Evenings at Calvera Playhouse Recital Season

Calvera Playhouse Recital Season

Febraury 1st - Peter Hale Brandt (Vesta Winner, Harbor Kids)
March 1st - Celia Dunworth (Silver Lantern Winner, The Fern)
April 5th - Marisol Pike (A Toast to Nina: The First Decade)
May 3rd - Teresa Galloway (Vesta Nominee, Polly)

All shows at 7:30PM

Subscribe to the series and save 10%

Get your tickets online at www.velbrookstages.com

Poster size 11" X 17" also 27" x 41"

Target Market(s)

Upscale market and music lovers. Small venue with international performers

Colors

Designer to choose colors to be used in the design.

Requirements
Must have
• Upscale - rich - style - like DIVA
Should not have
• Clip art

```html
<!DOCTYPE html>
<html lang="en">
<head>
<meta charset="utf-8">
<title>Calvera Playhouse Recital Season</title>
<link href="https://fonts.googleapis.com/css2?family=Inter:wght@400;600;700;800;900&display=swap" rel="stylesheet">
<style>
  :root {
    --page: #e9e8e5;
    --ink: #050505;
    --white: #ffffff;
    --magenta: #e5138c;
    --cyan: #1aa9e6;
    --green: #3aaa3e;
    --orange: #f39c12;
    --gold: #f2a516;
    --mural-dark: #2a130c;
    --mural-red: #8a2a18;
    --mural-orange: #c8622a;
    --mural-teal: #8fb9b4;
  }
  * { box-sizing: border-box; margin: 0; padding: 0; }
  html, body {
    width: 1200px; height: 1200px; overflow: hidden;
    background: var(--page);
    font-family: "Inter", Arial, sans-serif;
  }
  .poster {
    position: absolute; left: 220px; top: 40px;
    width: 760px; height: 1120px;
    background: var(--ink);
    overflow: hidden;
  }
  .mural {
    position: absolute; left: 0; top: 0; width: 760px; height: 540px;
    background:
      radial-gradient(ellipse 180px 260px at 470px 330px, rgba(143,185,180,.75), transparent 70%),
      radial-gradient(ellipse 220px 200px at 560px 200px, rgba(200,98,42,.8), transparent 70%),
      radial-gradient(ellipse 300px 320px at 400px 300px, var(--mural-red), transparent 75%),
      linear-gradient(90deg, #4a2a18 0%, var(--mural-dark) 12%, #5a2416 50%, var(--mural-dark) 88%, #4a2a18 100%);
  }
  .mural::after {
    content: ""; position: absolute; inset: 0;
    background: linear-gradient(180deg, var(--ink) 0%, rgba(5,5,5,0) 18%, rgba(5,5,5,0) 88%, var(--ink) 100%);
  }
  .title {
    position: absolute; left: 48px; top: 44px;
    font-weight: 800; font-size: 96px; line-height: 84px;
    letter-spacing: -4px;
  }
  .title .venue { color: var(--white); display: block; }
  .title .season {
    color: var(--magenta); display: block;
    -webkit-text-stroke: 6px var(--white);
    paint-order: stroke fill;
  }
  .lineup {
    position: absolute; left: 40px; top: 540px; width: 680px;
    display: flex; gap: 8px;
  }
  .act { flex: 1; }
  .act-head {
    height: 88px; color: var(--white); text-align: center;
    padding-top: 10px; line-height: 1.15;
  }
  .act-date { font-size: 16px; font-weight: 400; }
  .act-name { font-size: 15px; font-weight: 700; text-transform: uppercase; white-space: nowrap; }
  .act-note { font-size: 10px; font-weight: 400; }
  .act-show { font-size: 12px; font-weight: 400; }
  .act--cyan .act-head { background: var(--cyan); }
  .act--green .act-head { background: var(--green); }
  .act--orange .act-head { background: var(--orange); }
  .act--magenta .act-head { background: var(--magenta); }
  .portrait { height: 250px; }
  .portrait--light { background: linear-gradient(160deg, #f4f4f4, #dcdcdc); }
  .portrait--grey { background: linear-gradient(160deg, #6a6a6a, #2a2a2a); }
  .portrait--red { background: linear-gradient(160deg, #7a1d14, #3a0e0a); }
  .portrait--pink { background: linear-gradient(160deg, #f6dbe8, #e6b9cf); }
  .showtime {
    position: absolute; left: 0; top: 888px; width: 760px; text-align: center;
    color: var(--gold); font-weight: 700; font-size: 20px; letter-spacing: 4px;
  }
  .footer {
    position: absolute; left: 0; top: 930px; width: 760px; height: 190px;
    background:
      linear-gradient(90deg, #1b2a2e 0%, #1f2a22 28%, #2a2218 52%, #2a1020 76%, #1a0a14 100%);
  }
  .footer::before {
    content: ""; position: absolute; inset: 0;
    background: linear-gradient(180deg, rgba(5,5,5,.2), rgba(5,5,5,.85));
  }
  .footer-copy {
    position: absolute; left: 0; top: 34px; width: 760px; text-align: center;
    color: var(--white); font-weight: 600; font-size: 19px; line-height: 44px;
  }
</style>
</head>
<body>
  <main class="poster" aria-label="Evenings at Calvera Playhouse Recital Season">
    <div class="mural" role="img" aria-label="Painted theatre mural of a dancer with flowing teal drapery over red and orange ornament"></div>
    <h1 class="title">
      <span class="venue">Calvera<br>Playhouse</span>
      <span class="season">Recital<br>Season</span>
    </h1>

    <section class="lineup">
      <article class="act act--cyan">
        <header class="act-head">
          <div class="act-date">Febraury 1st</div>
          <div class="act-name">Peter Hale Brandt</div>
          <div class="act-note">Vesta Winner</div>
          <div class="act-show">Harbor Kids</div>
        </header>
        <div class="portrait portrait--light" role="img" aria-label="Portrait photo of Peter Hale Brandt"></div>
      </article>
      <article class="act act--green">
        <header class="act-head">
          <div class="act-date">March 1st</div>
          <div class="act-name">Celia Dunworth</div>
          <div class="act-note">Silver Lantern Winner</div>
          <div class="act-show">The Fern</div>
        </header>
        <div class="portrait portrait--grey" role="img" aria-label="Portrait photo of Celia Dunworth"></div>
      </article>
      <article class="act act--orange">
        <header class="act-head">
          <div class="act-date">April 5th</div>
          <div class="act-name">Marisol Pike</div>
          <div class="act-note">A Toast to Nina</div>
          <div class="act-show">The First Decade</div>
        </header>
        <div class="portrait portrait--red" role="img" aria-label="Portrait photo of Marisol Pike"></div>
      </article>
      <article class="act act--magenta">
        <header class="act-head">
          <div class="act-date">May 3rd</div>
          <div class="act-name">Teresa Galloway</div>
          <div class="act-note">Vesta Nominee</div>
          <div class="act-show">Polly</div>
        </header>
        <div class="portrait portrait--pink" role="img" aria-label="Portrait photo of Teresa Galloway"></div>
      </article>
    </section>

    <p class="showtime">ALL SHOWS AT 7:30PM</p>

    <footer class="footer">
      <p class="footer-copy">Subscribe to the series and save 10%<br>Get your tickets online at www.velbrookstages.com</p>
    </footer>
  </main>
</body>
</html>
```